Rackcard for That Dusty Granary event

We're a small nonprofit reuse center for home improvement supplies. We pick up donations of unwanted and salvaged building materials throughout the metro DC region. Then, we make the building materials available to the public at low cost, and provide vintage materials for restoring old homes. We also offer public education about reuse, and distribute free supplies to local nonprofits and neighbors in need.
Our free annual event, That Dusty Granary, is a old-timey fall festival that celebrates all things vintage (architectural salvage, restoring historic homes, antique appraisal, etc).
We're looking for a rackcard design for this year's event that will be used to invite the general public to our event. We usually prefer to stay away from photography in our flyers (as it can look very "stock image" cheesy), but we're interested in seeing any proposals you have.
Attached is the approved wording for our rackcard.
You can see more about Harbor Pallet at HarborPallet.org

Target Market(s)

Historic home owners, antique collectors/dealers, historic society members, local history buffs, architecture enthusiasts, families (all ages), folks who just like vintage stuff.

Industry/Entity Type

Non Profit

Font styles to use
Serif
Decorative
Script

Requirements
Must have
• Copy is preapproved and must be used exactly.
• Size of rackcard must be 5x7 inches. But can be landscape or portrait.
Nice to have
• See reference files for colors desired - these photos are for color suggestions, they're not intended to suggest design. Though they are very nice looking designs as well.
• Turquoise, browns, cedar, salmon, oranges, reds, etc.
• Antique house, architectural salvage, tools, etc. implied in the art work. Wood, old-fashioned wallpaper, skeleton keys, brick, and crown molding are some ideas.
• This is also a fall event, touches of an old-time fall festival would be nice.
Should not have
• We usually prefer to not use photos of people or places. Most flyers with photos look very "stock-photo" like and cheap. But, if you are extremely skilled with blending photos into an attractive event flyer then we're willing to take a look at all design options.
• I've attached some reference photos for ideas as well.

```html
<!DOCTYPE html>
<html lang="en">
<head>
<meta charset="utf-8">
<title>That Dusty Granary – Rackcard</title>
<link rel="stylesheet" href="https://fonts.googleapis.com/css2?family=Almendra:wght@400;700&family=Roboto+Slab:wght@500;700;800&family=Old+Standard+TT:ital,wght@0,400;0,700;1,400&display=swap">
<style>
  :root {
    --wood-dark: #6a4527;
    --wood-mid: #8f6340;
    --wood-light: #a97c55;
    --plank-seam: rgba(60, 35, 15, .35);
    --plank-grain: rgba(255, 230, 200, .07);
    --board-light: #ecd9b8;
    --board-mid: #d9bb92;
    --board-edge: #b58c5f;
    --ink-brown: #3d2716;
    --badge-orange: #f4a72f;
    --badge-rim: #c9741a;
    --teal: #4fb3b0;
    --teal-dark: #2f8f8d;
    --cream: #f6ead2;
    --feature-orange: #f7a530;
    --feature-outline: #7a4a10;
    --leaf-brown: #8a4f1c;
    --rope: #6b4a2e;
  }
  * { margin: 0; padding: 0; box-sizing: border-box; }
  html, body { width: 885px; height: 1200px; overflow: hidden; }
  body { position: relative; font-family: "Old Standard TT", serif; background: var(--wood-mid); }

  .wood-backdrop {
    position: absolute; inset: 0;
    background:
      repeating-linear-gradient(180deg, transparent 0 116px, var(--plank-seam) 116px 120px),
      repeating-linear-gradient(180deg, transparent 0 13px, var(--plank-grain) 13px 15px),
      linear-gradient(180deg, var(--wood-light) 0%, var(--wood-mid) 55%, var(--wood-dark) 100%);
  }

  .butterfly-art {
    position: absolute; left: 82px; top: 64px; width: 272px; height: 243px;
    background: radial-gradient(ellipse at center, #a9cdd0 0%, #d4b27a 55%, rgba(212,178,122,0) 72%);
    border-radius: 50%;
  }

  .hanger { position: absolute; left: 0; top: 0; width: 885px; height: 500px; }

  .sign-board {
    position: absolute; left: 92px; top: 400px; width: 748px; height: 345px;
    background: linear-gradient(180deg, var(--board-light) 0%, var(--board-mid) 100%);
    border: 4px solid var(--board-edge);
    border-radius: 6px;
    box-shadow: 5px 9px 16px rgba(40,20,5,.5);
    transform: rotate(2.5deg);
    text-align: center;
    color: var(--ink-brown);
    padding-top: 30px;
  }
  .event-title { font-family: "Almendra", serif; font-weight: 700; font-size: 64px; line-height: 1; }
  .event-subtitle { font-family: "Almendra", serif; font-weight: 700; font-size: 40px; line-height: 1.15; margin-top: 10px; }
  .divider { display: block; margin: 10px auto 6px; }
  .venue { font-family: "Roboto Slab", serif; font-weight: 700; font-size: 23px; line-height: 1.22; }

  .date-badge {
    position: absolute; left: 592px; top: 18px; width: 262px; height: 262px;
    border-radius: 50%;
    background: var(--badge-orange);
    border: 7px solid var(--badge-rim);
    box-shadow: 0 0 0 5px var(--cream), 4px 8px 14px rgba(40,20,5,.45);
    color: var(--ink-brown);
    text-align: center;
    font-family: "Roboto Slab", serif;
    padding-top: 36px;
  }
  .date-badge .day { font-size: 31px; font-weight: 800; }
  .date-badge .date { font-size: 38px; font-weight: 800; line-height: 1.15; }
  .date-badge .time { font-size: 27px; font-weight: 800; }
  .badge-leaves {
    display: block; margin: 10px auto 0; width: 74px; height: 40px;
    border-radius: 50%;
    background: radial-gradient(ellipse at center, var(--leaf-brown) 0%, rgba(138,79,28,.4) 60%, rgba(138,79,28,0) 75%);
  }

  .feature-label { position: absolute; left: 59px; top: 752px; width: 767px; height: 266px; }
  .feature-label svg { position: absolute; inset: 0; }
  .feature-text { position: absolute; inset: 0; text-align: center; padding: 34px 60px 0; }
  .feature-heading { font-family: "Almendra", serif; font-weight: 700; font-size: 46px; color: var(--cream); line-height: 1; }
  .feature-list {
    list-style: none; margin-top: 10px;
    font-family: "Roboto Slab", serif; font-weight: 800;
    font-size: 22px; line-height: 1.2;
    color: var(--feature-orange);
    text-shadow: 0 1px 0 var(--feature-outline), 1px 0 0 var(--feature-outline), -1px 0 0 var(--feature-outline), 0 -1px 0 var(--feature-outline);
  }
  .feature-list .aside { font-size: 17px; }
  .label-leaves {
    position: absolute; top: 178px; width: 82px; height: 46px; border-radius: 50%;
    background: radial-gradient(ellipse at center, var(--leaf-brown) 0%, rgba(138,79,28,.4) 60%, rgba(138,79,28,0) 75%);
  }
  .label-leaves.left { left: 36px; }
  .label-leaves.right { right: 36px; }

  .contact {
    position: absolute; left: 0; width: 885px; top: 1050px;
    text-align: center;
    font-family: "Roboto Slab", serif; font-weight: 700;
    font-size: 22px; line-height: 1.55; color: var(--badge-orange);
  }
</style>
</head>
<body>
  <div class="wood-backdrop" role="img" aria-label="Weathered wooden plank wall background"></div>

  <div class="butterfly-art" role="img" aria-label="Illustration of a teal and cream butterfly"></div>

  <svg class="hanger" viewBox="0 0 885 500" aria-hidden="true">
    <line x1="383" y1="117" x2="190" y2="410" stroke="var(--rope)" stroke-width="8" stroke-linecap="round"/>
    <line x1="383" y1="117" x2="560" y2="420" stroke="var(--rope)" stroke-width="8" stroke-linecap="round"/>
    <circle cx="383" cy="117" r="14" fill="#4a4a4a" stroke="#222" stroke-width="2"/>
    <circle cx="379" cy="113" r="4" fill="#9a9a9a"/>
  </svg>

  <section class="sign-board">
    <h1 class="event-title">That Dusty Granary:</h1>
    <p class="event-subtitle">A Celebration of Old Homes and<br>the Folks Who Love Them</p>
    <svg class="divider" width="240" height="18" viewBox="0 0 240 18" aria-hidden="true">
      <path d="M10 9 Q60 0 120 9 Q180 18 230 9" fill="none" stroke="var(--ink-brown)" stroke-width="2.5"/>
      <circle cx="120" cy="9" r="4" fill="var(--ink-brown)"/>
    </svg>
    <p class="venue">at Harbor Pallet's Reuse Warehouse<br>2280 Larkspur Lane, Millbrook MD 20799<br>Just 5 min. from DC in the Millbrook area!</p>
  </section>

  <div class="date-badge">
    <div class="day">SATURDAY</div>
    <div class="date">Sept. 12th,</div>
    <div class="time">10am – 3pm</div>
    <span class="badge-leaves" role="img" aria-label="Small autumn leaf ornament"></span>
  </div>

  <section class="feature-label">
    <svg viewBox="0 0 767 266" aria-hidden="true">
      <path d="M40 0 H727 Q727 40 767 40 V226 Q727 226 727 266 H40 Q40 226 0 226 V40 Q40 40 40 0 Z" fill="var(--cream)"/>
      <path d="M52 12 H715 Q717 50 755 52 V214 Q717 216 715 254 H52 Q50 216 12 214 V52 Q50 50 52 12 Z" fill="var(--teal)" stroke="var(--teal-dark)" stroke-width="3"/>
    </svg>
    <span class="label-leaves left" role="img" aria-label="Autumn leaf ornament"></span>
    <span class="label-leaves right" role="img" aria-label="Autumn leaf ornament"></span>
    <div class="feature-text">
      <h2 class="feature-heading">~ Featuring ~</h2>
      <ul class="feature-list">
        <li>Antique Experts, Preservation &amp; Appraisal Advice,<br>and Free Workshops</li>
        <li>Old-Timey Bands, Food, and Cider and a<br>Rare Opportunity to view our large<br>selection of Vintage Tools<br><span class="aside">(normally sold only online)</span></li>
      </ul>
    </div>
  </section>

  <footer class="contact">
    <p>Questions? www.HarborPallet.org</p>
    <p>301-555-0142 or Outreach@HarborPallet.org</p>
  </footer>
</body>
</html>
```